Content processing platform needs a landing page for products

We need a general landing page for products that we are launching. The concept of the product page is to do two things: a) Get users to sign up for our waitlist (que) so they get access to the product (we give access weekly). b) To generate interest for future products that we have not decided on yet. Mockups: Please see our mockups for inspiration. You have pretty free hands to combine, but please don't let our users think :-). Style: Please use the colours of our style sheet and see the home page (penlyhub.com) for inspiration on how we want the style and tone to be. The final design should communicate "scaling".

Target Market(s)

B2B - online businesses big and small that wish to scale their production of content and translation.

Industry/Entity Type

SaaS

Number of Pages Required

1 page

Font styles to use
Other font styles liked:
• open sans

Requirements
Must have
• Follow our styleguide.

```html
<!DOCTYPE html>
<html lang="en">
<head>
<meta charset="utf-8">
<title>Penlyhub – Scale Searchly Ads</title>
<link href="https://fonts.googleapis.com/css2?family=Open+Sans:wght@400;600;700&family=Roboto:wght@400;500&display=swap" rel="stylesheet">
<style>
:root{
  --blue:#1a9be0;
  --blue-band:#1c73c6;
  --green-band:#1a7a4e;
  --pink:#f0245b;
  --ink:#1d1d1d;
  --hero-bg:#ececec;
  --tab-dark:#222;
  --teal:#28b59f;
  --sky:#5dc1ec;
  --footer:#111;
  --footer-bottom:#0a0a0a;
  --gold:#f7c21b;
}
*{box-sizing:border-box;margin:0;padding:0}
html,body{width:1200px;height:3243px;overflow:hidden}
body{font-family:"Open Sans",Arial,sans-serif;color:var(--ink);background:#fff;position:relative}
.abs{position:absolute}

/* header */
.site-header{position:absolute;left:0;top:0;width:1200px;height:115px;background:#fff;box-shadow:0 2px 6px rgba(0,0,0,.12);z-index:2}
.brand{left:91px;top:36px;display:flex;align-items:center;gap:10px;font-weight:700;font-size:31px;color:var(--blue)}
.brand-dot{width:14px;height:14px;background:var(--blue);border-radius:50%}
.main-nav{left:317px;top:42px;display:flex;gap:24px;font-size:16px;color:#333}
.nav-btn{top:37px;height:39px;border:2px solid;display:flex;align-items:center;justify-content:center;font-size:13px;font-weight:600}
.nav-btn.scale{left:755px;width:170px;border-color:var(--blue);color:var(--blue)}
.nav-btn.freelance{left:938px;width:171px;border-color:var(--pink);color:var(--pink)}

/* hero */
.hero{position:absolute;left:0;top:115px;width:1200px;height:545px;background:var(--hero-bg)}
.hero-mark{left:87px;top:60px;width:64px;height:54px}
.hero-title{left:166px;top:90px;font-size:19px;color:#333}
.video{left:91px;top:155px;width:469px;height:316px;border:2px solid #c3304f;background:linear-gradient(135deg,#6b4a3c,#c8a58a 55%,#e9ddd2);box-shadow:0 3px 8px rgba(0,0,0,.2)}
.play{position:absolute;left:200px;top:122px;width:68px;height:68px;border-radius:50%;background:rgba(20,20,20,.75)}
.play::after{content:"";position:absolute;left:27px;top:20px;border-left:20px solid #fff;border-top:14px solid transparent;border-bottom:14px solid transparent}
.roi-card{left:582px;top:155px;width:527px;height:316px;background:#fff;border:2px solid #9cc2dd;box-shadow:0 3px 8px rgba(0,0,0,.15)}
.roi-card h2{position:absolute;top:22px;width:100%;text-align:center;font-size:20px;font-weight:600}
.roi-step{position:absolute;top:82px;width:140px;text-align:center;font-size:11px;line-height:16px;color:#333}
.roi-step svg{display:block;margin:0 auto 20px}
.email-bar{display:flex;align-items:center;justify-content:space-between;background:#e8e8e8;border:2px solid #ccc;padding:0 6px 0 12px;font-size:14px;color:#333}
.email-bar .label::before{content:"✉ ";}
.cta{background:var(--pink);color:#fff;font-weight:600;display:flex;align-items:center;justify-content:center}
.roi-card .email-bar{position:absolute;left:34px;top:239px;width:459px;height:43px}
.roi-card .cta{width:120px;height:33px;font-size:13px}

/* tabs */
.tabs{left:151px;top:724px;width:911px;height:69px;display:flex;font-size:25px;font-weight:600;color:#fff}
.tab{display:flex;align-items:center;justify-content:center;background:var(--tab-dark)}
.tab.active{background:var(--blue);width:297px}
.tab.tab-reviews{width:356px;border-right:1px solid #444}
.tab.tab-stats{width:258px}
.tab-pointer{left:282px;top:793px;border-left:20px solid transparent;border-right:20px solid transparent;border-top:33px solid var(--blue)}

/* packages */
.section-title{width:1200px;text-align:center;font-weight:600;font-size:48px}
.packages-title{top:866px}
.packages-sub{top:938px;width:1200px;text-align:center;font-size:23px;color:#333}
.plan{top:1025px;width:240px;height:348px;border:2px solid #cfcfcf;border-radius:4px;background:#fff;box-shadow:0 2px 6px rgba(0,0,0,.12);text-align:center}
.plan h3{margin-top:22px;font-size:20px;font-weight:600;letter-spacing:.5px}
.plan .price{font-size:50px;font-weight:700;color:var(--pink);line-height:60px;margin-top:4px}
.plan .period{font-size:17px;color:#333}
.plan ul{list-style:none;text-align:left;margin:22px 0 0 26px;font-size:12px;line-height:15px;color:#333}
.plan li{position:relative;padding-left:18px;margin-bottom:13px}
.plan li::before{content:"";position:absolute;left:0;top:2px;width:10px;height:10px;border-radius:50%;background:var(--blue)}
.plan li.tight{margin-bottom:0}
.packages-email{position:absolute;left:324px;top:1420px;width:552px;height:52px}
.packages-email .cta{width:130px;height:38px;font-size:15px}

/* reviews & faq */
.reviews-band{left:0;top:1559px;width:588px;height:629px;background:linear-gradient(160deg,#1f86db,var(--blue-band) 60%,#1466b3)}
.faq-band{left:588px;top:1559px;width:612px;height:629px;background:linear-gradient(160deg,#1e8a5b,var(--green-band) 60%,#146a43)}
.band-title{position:absolute;top:62px;font-size:38px;font-weight:600;color:#fff}
.review{position:absolute;left:91px;width:441px;height:90px;background:#fff;display:flex}
.review .photo{width:96px;height:90px;background:linear-gradient(135deg,#8a6a55,#d2b49a);flex:none}
.review .body{padding:14px 0 0 16px;font-family:Roboto,"Open Sans",sans-serif;font-size:16px;color:#333}
.stars{color:var(--gold);font-size:30px;letter-spacing:1px;line-height:34px}
.faq-item{position:absolute;left:39px;width:482px;height:56px;background:#fff;display:flex;align-items:center;justify-content:space-between;padding:0 14px 0 26px;font-family:Roboto,"Open Sans",sans-serif;font-size:16px;color:#222}
.plus{width:18px;height:18px;background:var(--blue);border-radius:2px;position:relative;flex:none}
.plus::before,.plus::after{content:"";position:absolute;background:#fff}
.plus::before{left:4px;top:8px;width:10px;height:2px}
.plus::after{left:8px;top:4px;width:2px;height:10px}

/* stats */
.stats-title{top:2268px}
.chart{top:2380px;width:497px;height:312px;background:#fff;box-shadow:0 2px 10px rgba(0,0,0,.18)}
.chart text{font-family:"Open Sans",sans-serif;font-size:11px;fill:#333}

/* footer */
.footer-rule{left:0;top:2779px;width:1200px;height:9px;background:var(--pink)}
.site-footer{left:0;top:2788px;width:1200px;height:377px;background:var(--footer);color:#fff}
.footer-col{position:absolute;top:85px}
.footer-col h4{font-size:20px;font-weight:400;margin-bottom:20px}
.footer-col a{display:block;color:#fff;text-decoration:none;font-size:16px;line-height:34px}
.contact-block{position:relative;padding-left:36px;margin-bottom:30px;font-size:15px;line-height:22px}
.contact-block strong{font-size:16px;font-weight:600;display:block}
.contact-block svg{position:absolute;left:0;top:0}
.lang{font-size:20px;line-height:44px}
.lang.muted{color:#444}
.footer-bottom{left:0;top:3165px;width:1200px;height:78px;background:var(--footer-bottom);color:#aaa;font-size:14px;text-align:center;line-height:78px}
.chat{left:1091px;top:3182px;width:44px;height:44px;border-radius:50%;background:var(--pink)}
.chat::after{content:"";position:absolute;left:13px;top:12px;width:18px;height:18px;border-radius:3px;background:#fff}
</style>
</head>
<body>

<header class="site-header">
  <div class="abs brand"><span>Penlyhub</span><span class="brand-dot"></span></div>
  <nav class="abs main-nav"><span>Products</span><span>Apps</span><span>Prices</span><span>Blog</span><span>Help Center</span></nav>
  <div class="abs nav-btn scale">SCALE YOUR BUSINESS</div>
  <div class="abs nav-btn freelance">BECOME A FREELANCER</div>
</header>

<section class="hero">
  <svg class="abs hero-mark" viewBox="0 0 64 54" aria-hidden="true">
    <rect x="2" y="16" width="42" height="30" fill="none" stroke="#333" stroke-width="2"/>
    <rect x="16" y="46" width="14" height="4" fill="#333"/>
    <rect x="30" y="2" width="16" height="16" fill="#1a9be0"/>
    <rect x="50" y="24" width="10" height="14" fill="none" stroke="#333" stroke-width="2"/>
    <path d="M12 38l8-14 8 14z" fill="#1a9be0"/>
  </svg>
  <div class="abs hero-title">Scale Searchly Ads with penlyhub.com</div>

  <div class="abs video" role="img" aria-label="Video still: smiling man at a laptop in a bright office"><span class="play"></span></div>

  <div class="abs roi-card">
    <h2>Continuously improve ROI on your Searchly Ads</h2>
    <div class="roi-step" style="left:26px">
      <svg width="48" height="56" viewBox="0 0 48 56"><path d="M6 2h26l12 12v40H6z" fill="none" stroke="#1a9be0" stroke-width="2"/><path d="M13 20h24M13 28h24M13 36h24M13 44h16" stroke="#1a9be0" stroke-width="2"/></svg>
      Seamlessly connect your Searchly Ad Campaigns to penlyhub.com
    </div>
    <div class="roi-step" style="left:192px">
      <svg width="86" height="56" viewBox="0 0 86 56"><g fill="none" stroke="#1a9be0" stroke-width="2"><rect x="4" y="4" width="22" height="28"/><rect x="32" y="4" width="22" height="28"/><rect x="60" y="4" width="22" height="28"/><rect x="18" y="24" width="22" height="28"/><rect x="46" y="24" width="22" height="28"/></g></svg>
      Get split ad versions submitted to a Searchly Experiment each month
    </div>
    <div class="roi-step" style="left:358px">
      <svg width="56" height="56" viewBox="0 0 56 56"><g fill="none" stroke="#1a9be0" stroke-width="2"><rect x="4" y="8" width="40" height="40"/><circle cx="40" cy="16" r="12"/><path d="M10 40l10-12 8 6 12-14"/></g></svg>
      See guaranteed improvement on ad metrics each month
    </div>
    <div class="email-bar"><span class="label">Email</span><span class="cta">Get Early Access</span></div>
  </div>
</section>

<nav class="abs tabs">
  <div class="tab active">Packages</div>
  <div class="tab tab-reviews">Reviews &amp; FAQ</div>
  <div class="tab tab-stats">Stats</div>
</nav>
<div class="abs tab-pointer"></div>

<h2 class="abs section-title packages-title">Packages</h2>
<p class="abs packages-sub">Get better ad metrics each month with creative copy</p>

<div class="abs plan" style="left:91px">
  <h3>LOCAL</h3><div class="price">€ 42</div><div class="period">Per Month</div>
  <ul><li>1 Language</li><li>3 - 5 different writers</li><li>3 ads</li><li>9 - 15 ad copy variations /mo</li><li class="tight">1 - 3 winning experiments guaranteed each month</li></ul>
</div>
<div class="abs plan" style="left:352px">
  <h3>NATIONAL</h3><div class="price">€ 167</div><div class="period">Per Month</div>
  <ul><li>Up to 2 Languages</li><li>15+ different writers</li><li>5 ads</li><li>60 - 75 ad copy variations /mo</li><li class="tight">4 - 5 winning experiments guaranteed each month</li></ul>
</div>
<div class="abs plan" style="left:614px">
  <h3>MULTINATIONAL</h3><div class="price">€ 333</div><div class="period">Per Month</div>
  <ul><li>Up to 4 Languages</li><li>40+ different writers</li><li>36 ads</li><li>180 ad copy variations /mo</li><li class="tight">10 - 36 winning experiments guaranteed each month</li></ul>
</div>
<div class="abs plan" style="left:873px">
  <h3>GLOBAL</h3><div class="price">€ 999</div><div class="period">Per Month</div>
  <ul><li>Unlimited Languages</li><li>100+ different writers</li><li>140 ads</li><li>700 ad copy variations /mo</li><li class="tight">30 - 108 winning experiments guaranteed each month</li></ul>
</div>

<div class="email-bar packages-email"><span class="label">Email</span><span class="cta">Get Early Access</span></div>

<section class="abs reviews-band">
  <h2 class="band-title" style="left:91px">Reviews</h2>
  <div class="review" style="top:141px"><div class="photo" role="img" aria-label="Customer portrait"></div><div class="body">Neque porro quisquam est qui dolorem<div class="stars">★★★★★</div></div></div>
  <div class="review" style="top:244px"><div class="photo" role="img" aria-label="Customer portrait"></div><div class="body">Dolorem ipsum quia dolor sit amet,<div class="stars">★★★★★</div></div></div>
  <div class="review" style="top:347px"><div class="photo" role="img" aria-label="Customer portrait"></div><div class="body">Neque porro quisquam est qui dolorem<div class="stars">★★★★★</div></div></div>
  <div class="review" style="top:450px"><div class="photo" role="img" aria-label="Customer portrait"></div><div class="body">Dolorem ipsum quia dolor sit amet,<div class="stars">★★★★★</div></div></div>
</section>

<section class="abs faq-band">
  <h2 class="band-title" style="left:44px">FAQ</h2>
  <div class="faq-item" style="top:134px">Q : Sed accumsan mi et massa pulvinar, at faucibus ?<span class="plus"></span></div>
  <div class="faq-item" style="top:204px">Q : Donec nec nulla eu augue molestie suscipit eget ?<span class="plus"></span></div>
  <div class="faq-item" style="top:274px">Q : Nullam blandit ex sed ante facilisis, dictum massa ?<span class="plus"></span></div>
  <div class="faq-item" style="top:344px">Q : Aliquam in nisl eu magna congue faucibus quis nec ?<span class="plus"></span></div>
  <div class="faq-item" style="top:414px">Q : Praesent maximus lorem sed sem facilisis, auctor ?<span class="plus"></span></div>
  <div class="faq-item" style="top:484px">Q : Praesent maximus lorem sed sem facilisis, auctor ?<span class="plus"></span></div>
</section>

<h2 class="abs section-title stats-title">Stats</h2>

<svg class="abs chart" style="left:91px" viewBox="0 0 497 312">
  <g stroke="#ddd" stroke-dasharray="4 4"><line x1="55" y1="80" x2="480" y2="80"/><line x1="55" y1="127.5" x2="480" y2="127.5"/><line x1="55" y1="175" x2="480" y2="175"/><line x1="55" y1="222.5" x2="480" y2="222.5"/></g>
  <line x1="55" y1="270" x2="480" y2="270" stroke="#999"/>
  <g text-anchor="end"><text x="44" y="84">20K</text><text x="44" y="131">15K</text><text x="44" y="179">10K</text><text x="44" y="226">5K</text><text x="44" y="274">0</text></g>
  <g fill="var(--teal)"><rect x="68" y="184.5" width="16" height="85.5"/><rect x="129" y="137" width="16" height="133"/><rect x="189" y="137" width="16" height="133"/><rect x="250" y="99" width="16" height="171"/><rect x="311" y="146.5" width="16" height="123.5"/><rect x="371" y="123" width="16" height="147"/><rect x="432" y="89.5" width="16" height="180.5"/></g>
  <g fill="var(--sky)"><rect x="86" y="165.5" width="16" height="104.5"/><rect x="147" y="132" width="16" height="138"/><rect x="207" y="180" width="16" height="90"/><rect x="268" y="127.5" width="16" height="142.5"/><rect x="329" y="208" width="16" height="62"/><rect x="389" y="189" width="16" height="81"/><rect x="450" y="175" width="16" height="95"/></g>
  <rect x="115" y="100" width="40" height="22" fill="#fff" stroke="#ccc"/><text x="135" y="115" text-anchor="middle" font-size="10">14.2K</text>
  <g text-anchor="middle"><text x="85" y="292">Mon</text><text x="146" y="292">Tue</text><text x="206" y="292">Wed</text><text x="267" y="292">Thu</text><text x="328" y="292">Fri</text><text x="388" y="292">Sat</text><text x="449" y="292">Sun</text></g>
</svg>

<svg class="abs chart" style="left:614px" viewBox="0 0 497 312">
  <g stroke="#ddd" stroke-dasharray="4 4"><line x1="55" y1="80" x2="480" y2="80"/><line x1="55" y1="127.5" x2="480" y2="127.5"/><line x1="55" y1="175" x2="480" y2="175"/><line x1="55" y1="222.5" x2="480" y2="222.5"/></g>
  <line x1="55" y1="270" x2="480" y2="270" stroke="#999"/>
  <g text-anchor="end"><text x="44" y="84">20K</text><text x="44" y="131">15K</text><text x="44" y="179">10K</text><text x="44" y="226">5K</text><text x="44" y="274">0</text></g>
  <polyline points="85,165.5 146,156 206,208 267,165.5 328,89.5 388,127.5 449,84.75" fill="none" stroke="var(--teal)" stroke-width="2"/>
  <polyline points="85,222.5 146,213 206,165.5 267,198.75 328,217.75 388,146.5 449,132" fill="none" stroke="var(--sky)" stroke-width="2"/>
  <g fill="#fff" stroke="var(--teal)" stroke-width="2"><circle cx="85" cy="165.5" r="4"/><circle cx="146" cy="156" r="4"/><circle cx="206" cy="208" r="4"/><circle cx="267" cy="165.5" r="4"/><circle cx="328" cy="89.5" r="4"/><circle cx="388" cy="127.5" r="4"/><circle cx="449" cy="84.75" r="4"/></g>
  <g fill="#fff" stroke="var(--sky)" stroke-width="2"><circle cx="85" cy="222.5" r="4"/><circle cx="146" cy="213" r="4"/><circle cx="206" cy="165.5" r="5"/><circle cx="267" cy="198.75" r="4"/><circle cx="328" cy="217.75" r="4"/><circle cx="388" cy="146.5" r="4"/><circle cx="449" cy="132" r="4"/></g>
  <rect x="188" y="128" width="36" height="22" fill="#fff" stroke="#ccc"/><text x="206" y="143" text-anchor="middle" font-size="10">11K</text>
  <g text-anchor="middle"><text x="85" y="292">Mon</text><text x="146" y="292">Tue</text><text x="206" y="292">Wed</text><text x="267" y="292">Thu</text><text x="328" y="292">Fri</text><text x="388" y="292">Sat</text><text x="449" y="292">Sun</text></g>
</svg>

<div class="abs footer-rule"></div>
<footer class="abs site-footer">
  <div class="footer-col" style="left:95px">
    <h4>CONTACT US</h4>
    <div class="contact-block">
      <svg width="24" height="30" viewBox="0 0 24 30"><path d="M12 2a9 9 0 0 0-9 9c0 7 9 17 9 17s9-10 9-17a9 9 0 0 0-9-9z" fill="none" stroke="#fff" stroke-width="1.6"/><circle cx="12" cy="11" r="3.5" fill="none" stroke="#fff" stroke-width="1.6"/></svg>
      <strong>ADDRESS</strong>Harborlaan 114 2041 KT Veldmere,<br>The Netherlands
    </div>
    <div class="contact-block">
      <svg width="24" height="24" viewBox="0 0 24 24"><path d="M5 2l4 1 1 5-3 2a13 13 0 0 0 7 7l2-3 5 1 1 4c-1 2-3 3-5 3C9 22 2 15 2 7c0-2 1-4 3-5z" fill="none" stroke="#fff" stroke-width="1.6"/></svg>
      <strong>PHONE NUMBER</strong>+31 (0)20 555 0172
    </div>
  </div>
  <div class="footer-col" style="left:432px">
    <h4>PENLYHUB</h4>
    <a>About Us</a><a>Team</a><a>Contact</a><a>Terms of Service</a><a>Privacy Policy</a><a>Imprint</a>
  </div>
  <div class="footer-col" style="left:668px">
    <h4>RESOURCES</h4>
    <a>Penlyhub Affiliate</a><a>Careers</a><a>Developer Resources</a><a>Penlyhub Workshops</a><a>Help</a>
  </div>
  <div class="footer-col" style="left:986px;top:76px">
    <div class="lang">ENGLISH</div>
    <div class="lang muted">TÜRKÇE</div>
  </div>
</footer>
<div class="abs footer-bottom">© 2018 Company Name &nbsp;All right reserved</div>
<div class="abs chat"></div>

</body>
</html>
```